Summer Sale Graphics for Social Media

I want to create 11 social media graphics (new Instagram size 4:5 (1080 x 1350 pixels) focusing on our Summer Sale Graphics, using any of the pics attached. Use the attached pics, NO RANDOM STOCK PHOTOGRAPHY. For the color scheme of the graphics, they should all be complementary to the product colors in the photos.
You can add any of the photos attached but none are required. You can do some of the graphics in all text. I mainly need BOLD text that says one of the headlines (11 total) SEE ATTACHED WORD DOCUMENT for the headlines to use.

```html
<!DOCTYPE html>
<html lang="en">
<head>
<meta charset="utf-8">
<title>Summer Sale Social Graphics</title>
<link href="https://fonts.googleapis.com/css2?family=Sorts+Mill+Goudy&family=Raleway:wght@700&family=Oswald:wght@500&family=Great+Vibes&display=swap" rel="stylesheet">
<style>
  :root {
    --bg: #d9d9d9;
    --paper: #ffffff;
    --red: #e4262b;
    --plum: #7a3a5e;
    --blue: #1f75bc;
    --green: #26362f;
    --ink: #111111;
  }
  * { box-sizing: border-box; margin: 0; padding: 0; }
  html, body { width: 1200px; height: 4051px; overflow: hidden; background: var(--bg); }
  .sheet {
    position: absolute; left: 98px; top: 104px;
    display: grid;
    grid-template-columns: 494px 494px;
    grid-auto-rows: 617px;
    column-gap: 24px; row-gap: 20px;
  }
  .card { position: relative; background: var(--paper); }
  .frame {
    position: absolute; inset: 31px;
    border: 3px solid var(--accent);
    border-radius: 3px;
    display: flex; flex-direction: column; align-items: center; justify-content: center;
    text-align: center; color: var(--accent);
  }
  .red { --accent: var(--red); }
  .plum { --accent: var(--plum); }
  .blue { --accent: var(--blue); }
  .green { --accent: var(--green); }

  .badge {
    width: 120px; height: 120px; border-radius: 50%;
    background: var(--accent); color: #fff;
    display: flex; flex-direction: column; align-items: center; justify-content: center;
    font-family: "Oswald", sans-serif; font-weight: 500;
    font-size: 27px; line-height: 1.25; letter-spacing: -0.5px;
    margin: 10px 0 18px;
  }
  .headline {
    font-family: "Sorts Mill Goudy", serif;
    color: var(--ink);
    font-size: 56px; line-height: 1.05; letter-spacing: 1px;
  }
  .tagline {
    font-family: "Raleway", sans-serif; font-weight: 700;
    font-size: 38px; line-height: 1.3; letter-spacing: -0.5px;
    margin-top: 6px;
  }
  .button {
    background: var(--accent); color: #fff; border-radius: 4px;
    font-family: "Great Vibes", cursive;
    font-size: 30px; line-height: 1;
    padding: 6px 26px 8px; margin-top: 12px;
  }
  .button.large { font-size: 34px; line-height: 1.15; padding: 14px 56px; margin-top: 28px; }
  .button.wide { font-size: 52px; width: 334px; padding: 14px 0 18px; margin: 8px 0 20px; }
  .button.tag { font-size: 40px; padding: 4px 42px 6px; margin-bottom: 18px; }
  .spaced { margin: 18px 0; }
</style>
</head>
<body>
<main class="sheet">

  <article class="card red"><div class="frame">
    <div class="badge"><span>UP TO</span><span>$15 OFF</span></div>
    <h2 class="headline">Your Summer</h2>
    <p class="tagline">BODY WON’T WAIT</p>
    <span class="button">Sale Now !</span>
  </div></article>

  <article class="card plum"><div class="frame">
    <div class="badge"><span>UP TO</span><span>$15 OFF</span></div>
    <h2 class="headline">Final Countdown</h2>
    <p class="tagline">TO SUMMER</p>
    <span class="button">Sale Now !</span>
  </div></article>

  <article class="card blue"><div class="frame">
    <div class="badge"><span>UP TO</span><span>$15 OFF</span></div>
    <h2 class="headline">Summer’s Here.</h2>
    <p class="tagline">AND WE’RE HAVING</p>
    <span class="button large">the Biggest Sale<br>of the Year</span>
  </div></article>

  <article class="card green"><div class="frame">
    <div class="badge"><span>UP TO</span><span>$15 OFF</span></div>
    <h2 class="headline">One Sale.<br>One Body.</h2>
    <p class="tagline">ONE SUMMER<br>TO SLAY</p>
  </div></article>

  <article class="card green"><div class="frame">
    <div class="badge"><span>UP TO</span><span>$15 OFF</span></div>
    <h2 class="headline">Summer Isn’t<br>Waiting</h2>
    <p class="tagline">NEITHER SHOULD<br>YOU</p>
    <span class="button">Sale Now !</span>
  </div></article>

  <article class="card blue"><div class="frame">
    <div class="badge"><span>UP TO</span><span>$15 OFF</span></div>
    <h2 class="headline">Slim Waist.<br>Flat Tummy.</h2>
    <p class="tagline">MORE ENERGY.<br>LET’S GO!</p>
    <span class="button">Sale Now !</span>
  </div></article>

  <article class="card red"><div class="frame">
    <h2 class="headline">Hurry!<br>Our Summer</h2>
    <p class="tagline">SLIM-DOWN</p>
    <span class="button">Sale Is On</span>
    <p class="tagline" style="margin-top:18px">DON’T MISS IT!</p>
    <div class="badge" style="margin-bottom:0"><span>UP TO</span><span>$15 OFF</span></div>
  </div></article>

  <article class="card plum"><div class="frame">
    <span class="button tag">Sale</span>
    <h2 class="headline">Your Summer</h2>
    <p class="tagline">BODY STARTS HERE</p>
    <div class="badge spaced"><span>UP TO</span><span>$15 OFF</span></div>
  </div></article>

  <article class="card blue"><div class="frame">
    <h2 class="headline">Limited-Time</h2>
    <span class="button wide">Summer Sale</span>
    <p class="tagline">SNATCH YOUR<br>SUPPLEMENTS<br>NOW!</p>
    <div class="badge" style="margin-bottom:0"><span>UP TO</span><span>$15 OFF</span></div>
  </div></article>

  <article class="card green"><div class="frame">
    <h2 class="headline">Get Snatched<br>for Summer</h2>
    <p class="tagline" style="margin-top:18px">SUPPLEMENTS ON</p>
    <span class="button" style="margin-top:18px">Sale Now !</span>
    <div class="badge" style="margin-top:24px;margin-bottom:0"><span>UP TO</span><span>$15 OFF</span></div>
  </div></article>

  <article class="card plum"><div class="frame">
    <div class="badge"><span>UP TO</span><span>$15 OFF</span></div>
    <h2 class="headline">Detox, Burn Fat,</h2>
    <p class="tagline">AND TURN HEADS<br>THIS SUMMER</p>
    <span class="button">Sale Now !</span>
  </div></article>

</main>
</body>
</html>
```